New Website for consulting company

We need a completely new design for our company web site: www.morvane-partners.ch (please do not use it as a reference. We want something completely different.)
We are a consulting company and therefore our team is our key ressource together with our skills.
This site will be german in the first place. It will be the webmasters job to create it multilingual.
The website should be rather eccentric but still informative.
For colors and logo please refer to attached Logodefinition.pdf. The colored horizontal logo should be somehow used for the website but doesn't need to be extremely prominent. You can choose every color for the design but the logo must be somehow embedded in original colors and the green should be integrated for the site.
Please keep in mind that it should also work for mobile devices so the webmaster will have to create a responsive website out of the submitted design.
The main Page should be a one pager with different layout blocks directly accessible via top sticky menubar.:
- AKTEURE (team), gallery, people centric with images of member and expandable description box, plus skills abstract list (name & description). See attached mockups to support the explaining (do not take it as a reference).
- ÜBER UNS (mission), Description of companies vision, mission, competences etc.
- ... according to the menu bar
We would like to have at least 3 different block layouts to fill with content for the one pager site:
1. Team is the most important and the least generic one
2. Big picture less text
3. Multiple smaller pictures multiple text blocks
4. Hardly any picture text centric
The page should communicate competence in what we are doing, quality and not least youth and freshness.
See Attachements:
- Logodefinition.pdf: Logo definition containing definition of color of the logo.
- mockup_Website_mock1.png: These should give you an impression of how it is meant to have layouted blocks

```html
<!DOCTYPE html>
<html lang="en">
<head>
<meta charset="utf-8">
<title>Morvane Partners</title>
<link href="https://fonts.googleapis.com/css2?family=Lato:wght@300;400;700;900&display=swap" rel="stylesheet">
<style>
:root{
  --green:#6cbd45;
  --green-dark:#5aa936;
  --ink:#3a3a3a;
  --muted:#8a8a8a;
  --line:#d8d8d8;
  --dark:#1d1d1d;
  --white:#ffffff;
}
*{box-sizing:border-box;margin:0;padding:0}
html,body{width:1200px;height:2479px;overflow:hidden}
body{font-family:"Lato",Arial,sans-serif;color:var(--ink);background:var(--white);position:relative}
.abs{position:absolute}

/* header */
.header{top:0;left:0;width:1200px;height:109px;background:var(--white)}
.brand{left:154px;top:25px;height:75px;display:flex;align-items:center;gap:14px}
.brand-mark{width:75px;height:75px;background:var(--green)}
.brand-name{font-size:30px;font-weight:700;color:var(--green);letter-spacing:.5px}
.social{display:flex;gap:7px}
.social span{width:24px;height:24px;display:block}
.social .s1{background:var(--green)}
.social .s2{background:#5b5b5b}
.social .s3{background:#8d8d8d}
.header .social{left:962px;top:50px}

/* nav */
.nav{top:109px;left:0;width:1200px;height:40px;border-top:4px solid var(--green);background:var(--white);border-bottom:1px solid #eee}
.nav ul{list-style:none;position:absolute;left:0;top:0;width:1200px;height:36px}
.nav li{position:absolute;top:0;height:36px;line-height:36px;font-size:13px;color:var(--ink);transform:translateX(-50%)}
.nav li.active{background:var(--green);color:var(--white);width:70px;text-align:center}
.dropdown{left:520px;top:149px;width:182px;background:var(--green);z-index:5}
.dropdown div{height:33px;line-height:33px;padding-left:22px;font-size:10px;font-weight:700;color:var(--white);border-bottom:1px solid rgba(255,255,255,.35)}
.dropdown div.current{background:var(--white);color:var(--green)}

/* hero */
.hero{top:149px;left:0;width:1200px;height:513px;background:radial-gradient(ellipse at 48% 40%,#8fbf4a 0%,#3f6a22 30%,#1e2c14 60%,#0d130a 100%)}
.hero-title{top:363px;left:0;width:1200px;text-align:center;font-size:30px;font-weight:900;color:var(--white);letter-spacing:1px}
.rule{width:50px;height:3px;background:var(--white);position:absolute;left:575px}
.hero-sub{top:440px;left:0;width:1200px;text-align:center;font-size:15px;color:var(--white);letter-spacing:.5px}
.arrow{width:26px;height:26px;top:399px}
.arrow.left{left:155px;background:rgba(80,80,80,.7)}
.arrow.right{left:1021px;background:var(--green)}
.dots{top:601px;left:586px;display:flex;gap:5px}
.dots span{width:8px;height:8px;border-radius:50%;background:var(--white)}
.dots span.on{background:var(--green)}

/* motivation */
.motivation{top:662px;left:0;width:1200px;height:285px;background:var(--green);color:var(--white);text-align:center}
.motivation h2{position:absolute;top:66px;width:1200px;font-size:26px;font-weight:300}
.motivation p{position:absolute;top:140px;left:230px;width:740px;font-size:13px;line-height:25px;font-weight:400}

/* tiles */
.tiles{top:947px;left:0;width:1200px;height:228px;display:flex}
.tile{width:400px;height:228px;position:relative;text-align:center;color:var(--white)}
.tile.t1{background:linear-gradient(135deg,#3a3a3a,#151515)}
.tile.t2{background:linear-gradient(135deg,#7a7a7a,#3a3a3a)}
.tile.t3{background:linear-gradient(135deg,#6d6d6d,#2a2a2a)}
.tile h3{position:absolute;top:90px;width:400px;font-size:22px;font-weight:400;letter-spacing:.5px}
.tile.t1 h3,.tile.t1 p{color:var(--green)}
.tile .trule{position:absolute;left:180px;top:124px;width:40px;height:2px;background:var(--white)}
.tile p{position:absolute;top:136px;width:400px;font-size:9px;font-weight:700}

/* consultant section */
.section-title{left:0;width:1200px;text-align:center;font-size:26px;font-weight:300;color:#555;line-height:32px}
.grule{width:40px;height:2px;background:#999;left:580px}
.body-text{font-size:12px;line-height:17px;color:var(--muted);text-align:center}
.intro{top:1240px}
.intro-text{top:1347px;left:230px;width:740px}
.intro-text p+p{margin-top:10px}
.btn{height:35px;border:1px solid #bdbdbd;font-size:10px;color:#777;text-align:center;line-height:33px;letter-spacing:.5px}
.btn-more{top:1468px;left:545px;width:115px}
.divider{top:1562px;left:0;width:1200px;height:4px;background:var(--green)}

/* team */
.team-title{top:1615px}
.team-text{top:1682px;left:330px;width:540px}
.card{top:1755px;width:228px;height:208px;background:linear-gradient(180deg,#f2f2f2,#dcdcdc)}
.card .caption{position:absolute;left:0;bottom:0;width:228px;height:49px;background:var(--dark);padding:17px 0 0 12px;font-size:10px;color:var(--white)}
.card .caption b{color:var(--green);font-weight:700;margin-right:8px}
.card .caption i{font-weight:700}
.card.open .caption{height:99px;background:rgba(25,25,25,.95)}
.card.open .caption p{margin-top:8px;font-size:8px;line-height:11px;color:#bbb;width:190px}
.card.open .caption u{display:block;margin-top:6px;font-size:8px;color:var(--green)}
.btn-all{top:2020px;left:553px;width:99px}

/* footer */
.footer{top:2120px;left:0;width:1200px;height:297px;background:linear-gradient(180deg,#2b2b2b,#121212);text-align:center;color:var(--white)}
.footer .social{position:absolute;left:562px;top:80px}
.footer h2{position:absolute;top:122px;width:1200px;font-size:34px;font-weight:300}
.footer .frule{position:absolute;left:580px;top:177px;width:40px;height:2px;background:var(--white)}
.footer address{position:absolute;top:195px;width:1200px;font-style:normal;font-size:11px;line-height:17px;color:#ddd}
.copyright{top:2417px;left:0;width:1200px;height:62px;background:var(--white);text-align:center;line-height:62px;font-size:9px;color:var(--muted)}
</style>
</head>
<body>

<header class="header abs">
  <div class="brand abs"><span class="brand-mark"></span><span class="brand-name">Morvane Partners</span></div>
  <div class="social abs"><span class="s1"></span><span class="s2"></span><span class="s3"></span></div>
</header>

<nav class="nav abs">
  <ul>
    <li style="left:191px">Home</li>
    <li style="left:278px">Competences</li>
    <li style="left:372px">Teams</li>
    <li style="left:466px">Customers</li>
    <li class="active" style="left:563px">Network</li>
    <li style="left:657px">Business</li>
    <li style="left:736px">Jobs</li>
    <li style="left:818px">Contact</li>
  </ul>
</nav>
<div class="dropdown abs">
  <div>Memberships</div>
  <div class="current">Partnerships</div>
  <div>Sponsoring</div>
</div>

<section class="hero abs" role="img" aria-label="Close-up photo of a green seedling sprouting from a seed among moss"></section>
<h1 class="hero-title abs">A COLLABORATION THAT BEARS FRUIT.</h1>
<span class="rule" style="top:420px"></span>
<p class="hero-sub abs">PROFOUND KNOWLEDGE AND INDEPENDENTLY.</p>
<span class="arrow left abs"></span>
<span class="arrow right abs"></span>
<div class="dots abs"><span class="on"></span><span></span><span></span></div>

<section class="motivation abs">
  <h2>Your success is our motivation.</h2>
  <span class="rule" style="top:113px"></span>
  <p>We think and act holistically and networked, methodical and structured. To get to Best Practices oriented, perfectly matched to your needs solutions. And so we continue to taste sweet and juicy Morvane Partners, we provide a regular fertilization in the form of consistent training.</p>
</section>

<section class="tiles abs">
  <div class="tile t1" role="img" aria-label="Photo of a business meeting in an office">
    <h3>COMPETENCIES</h3><span class="trule"></span><p>DUIS AUTE IRURE DOLOR IN REPREHENDERIT</p>
  </div>
  <div class="tile t2" role="img" aria-label="Photo of colleagues shaking hands">
    <h3>LATEST NEWS</h3><span class="trule"></span><p>DUIS AUTE IRURE DOLOR IN REPREHENDERIT</p>
  </div>
  <div class="tile t3" role="img" aria-label="Photo of documents and a pen on a desk">
    <h3>NETWORKS</h3><span class="trule"></span><p>DUIS AUTE IRURE DOLOR IN REPREHENDERIT</p>
  </div>
</section>

<h2 class="section-title intro abs">Transformed<br>The Idea of Consultant Services</h2>
<span class="grule abs" style="top:1325px"></span>
<div class="body-text intro-text abs">
  <p>Lorem ipsum dolor sit amet, consectetur adipiscing elit, sed do eiusmod tempor incididunt ut labore et dolore magna aliqua. Ut enim ad minim veniam, quis nostrud exercitation ullamco laboris nisi ut aliquip ex ea commodo consequat.</p>
  <p>Duis aute irure dolor in reprehenderit in voluptate velit esse cillum dolore eu fugiat nulla pariatur. Excepteur sint occaecat cupidatat non proident, sunt in culpa qui officia deserunt mollit anim id est laborum.</p>
</div>
<div class="btn btn-more abs">READ MORE</div>
<div class="divider abs"></div>

<h2 class="section-title team-title abs">Our Team</h2>
<span class="grule abs" style="top:1661px"></span>
<p class="body-text team-text abs">Duis aute irure dolor in reprehenderit in voluptate velit esse cillum dolore eu fugiat nulla pariatur. Excepteur sint occaecat cupidatat non proident</p>

<div class="card open abs" style="left:117px" role="img" aria-label="Portrait photo of the managing director">
  <div class="caption"><b>LUKAS M.</b><i>Managing Director</i>
    <p>We found this company to be very reasonable, efficient, and professional. Our home...</p><u>more</u></div>
</div>
<div class="card abs" style="left:367px" role="img" aria-label="Portrait photo of the graphic designer">
  <div class="caption"><b>SELINA W.</b><i>Graphic Designer</i></div>
</div>
<div class="card abs" style="left:612px" role="img" aria-label="Portrait photo of a project designer">
  <div class="caption"><b>MARCO B.</b><i>Project Designer</i></div>
</div>
<div class="card abs" style="left:860px" role="img" aria-label="Portrait photo of a project designer">
  <div class="caption"><b>JANA F.</b><i>Project Designer</i></div>
</div>
<div class="btn btn-all abs">VIEW ALL</div>

<footer class="footer abs" role="img" aria-label="Dark aerial photo of a city skyline">
  <div class="social"><span class="s1"></span><span class="s2"></span><span class="s3"></span></div>
  <h2>Morvane Partners</h2>
  <span class="frule"></span>
  <address>Morvane Partners AG, Postfach 4120, CH-3072 Ostermundigen<br>Phone: +41 31 555 01 23</address>
</footer>
<div class="copyright abs">Copyright © 2013 morvane-partners | privacy policy</div>

</body>
</html>
```